Flyer-Design virtueller Birchwood Circle
Zielgruppe
Gemeinnützige Non-Profit Organisation (SME Birchwood Circle) für kleine Beratungsunternehmen im deutschsprachigen Wirtschaftsraum.
Der SME Birchwood Circle bringt kleine und mittlere, aber hochqualifizierte Beratungsunternehmen zusammen.
Verkaufsaktivitäten rund um Kundenprojekte, offene Positionen und verfügbaren Kandidaten werden gemeinsam abgestimmt und angegangen.
Aufgabenstellung
Ich habe bereits mit dem Design eines Flyers angefangen (siehe Anlagen). Allerdings bin ich mit mir nicht zufrieden.
Der SME Birchwood Circle (Small and Medium Enterprises Birchwood Circle) oder KMU Lindenkreis (Lindenkreis für Kleine und Mittlere Unternehmen) besteht aus 3 Komponenten:
1. SME Call - zweiwöchentliche telefonische Abstimmung der Aktivitäten (wichtigste Komponente)
2. SME Event - Ungezwungenes und persönliches Treffen an einem Abend, resp. After Work Event
3. SME Platform - technische Plattform zum Austausch von Dokumenten (Offene Positionen und Lebensläufe von verfügbaren Kandidaten)
Diese 3 Komponenten laufen im SME BC zusammen, resp. diese bilden den SME BC.
Unsere Hauptfarbe Pantone 368 und das Logo (zeigt einen grünen Stammtisch mit grauen Stühlen) müssen verwendet werden. Ebenfalls ist der Text (Komponente 1 und 2) bereits in den Anlagen beschrieben. Für Komponente 3 (SME Platform) soll ein Platzhalter (50 Wörter) erstellt werden.
Ich suche ein finales Design für einen Flyer. Bin ich offen für das Format, gefaltet (Leporello oder Wickel), ich hätte A5, beidseitig gemacht oder ggf. in Visitenkartengrösse (85x55mm) für den leichteren Transport.

```html
<!DOCTYPE html>
<html lang="de">
<head>
<meta charset="utf-8">
<title>SME Birchwood Circle – Flyer 55x85 mm</title>
<link rel="stylesheet" href="https://fonts.googleapis.com/css2?family=Fira+Sans:wght@600;800&family=Source+Sans+3:wght@400;700&family=Noto+Sans+Mono&display=swap">
<style>
  :root{
    --green:#5bb02b;
    --green-dark:#4f9a26;
    --green-mid:#58a82a;
    --green-light:#72bb55;
    --grey-frame:#7c7c7c;
    --grey-photo-a:#d6d6d6;
    --grey-photo-b:#b9b9b9;
    --ink:#1e1e1e;
    --white:#ffffff;
    --shadow:0 4px 8px rgba(0,0,0,.35);
  }
  html,body{margin:0;padding:0;overflow:hidden;}
  body{width:1200px;height:1200px;background:var(--white);position:relative;font-family:"Source Sans 3",sans-serif;color:var(--ink);}
  .panel{position:absolute;box-shadow:var(--shadow);overflow:hidden;}
  .label{position:absolute;font-family:"Noto Sans Mono",monospace;font-size:23px;line-height:28px;color:#222;letter-spacing:.5px;}
  .photo{position:absolute;}
  .photo--table{background:radial-gradient(circle at 45% 50%, #f2f2f2 0 28%, var(--grey-photo-a) 29% 60%, var(--grey-photo-b) 100%);}
  .photo--meeting{background:linear-gradient(180deg,#dfe6ee 0%,#f0c7a0 40%,#e98a4a 55%,#3f6f86 80%,#9fc6d6 100%);}
  .badge{position:absolute;display:flex;align-items:center;justify-content:center;}
  .badge__ring{position:absolute;inset:0;border-radius:50%;background:var(--green);border:6px solid var(--white);box-sizing:border-box;}
  .badge__name{position:relative;font-family:"Fira Sans",sans-serif;font-weight:800;color:var(--white);text-align:center;line-height:.95;}
  .title-tag{position:absolute;background:var(--green);color:var(--white);font-family:"Fira Sans",sans-serif;font-weight:800;display:flex;align-items:center;justify-content:center;white-space:nowrap;}
  .contact{position:absolute;text-align:right;font-size:8.4px;line-height:11.2px;white-space:nowrap;}
  .contact__head{font-family:"Fira Sans",sans-serif;font-weight:800;font-size:8.6px;margin-bottom:24px;}
  .contact p{margin:0 0 11px;}
  .sender{position:absolute;display:flex;align-items:center;gap:5px;}
  .sender__mark{width:14px;height:14px;background:var(--green);}
  .sender__name{font-family:"Fira Sans",sans-serif;font-weight:800;font-size:20px;color:var(--green);}
  .intro{position:absolute;font-size:8.4px;line-height:11.2px;white-space:nowrap;}
  .intro b{font-weight:700;}
  .inner{color:var(--white);}
  .inner h2{font-family:"Fira Sans",sans-serif;font-weight:600;font-size:13px;margin:0 0 12px;}
  .inner h3{font-family:"Source Sans 3",sans-serif;font-weight:700;font-size:8.3px;line-height:11.2px;margin:0;}
  .inner p{font-size:8.3px;line-height:11.2px;margin:0 0 11px;white-space:nowrap;}
  .block{position:absolute;}
</style>
</head>
<body>

  <div class="label" style="left:905px;top:64px;">Format<br>55x85 mm</div>
  <div class="label" style="left:832px;top:350px;">aussen</div>
  <div class="label" style="left:638px;top:734px;">Titel/Rückseite</div>
  <div class="label" style="left:843px;top:1142px;">innen</div>

  <!-- Outside spread -->
  <section class="panel outside" style="left:111px;top:30px;width:664px;height:346px;background:var(--white);">
    <div style="position:absolute;left:0;top:0;width:216px;height:346px;background:var(--grey-frame);"></div>
    <div style="position:absolute;left:16px;top:17px;width:183px;height:313px;background:var(--white);"></div>
    <div class="intro" style="left:27px;top:64px;">Der <b>SME Birchwood Circle</b> bringt kleine<br>und mittlere, aber hochqualifizierte<br>Beratungsunternehmen zusammen.<br>Verkaufsaktivitäten rund um Kunden-<br>projekte, offene Positionen und verfüg-<br>baren Kandidaten werden gemeinsam<br>abgestimmt und angegangen. Jeder<br>Teilnehmer entwickelt hier sein Geschäft.</div>
    <div class="photo photo--meeting" role="img" aria-label="Silhouetten einer Geschäftsrunde an einem Konferenztisch im Gegenlicht" style="left:16px;top:183px;width:183px;height:115px;"></div>

    <div class="contact" style="right:355px;top:113px;">
      <div class="contact__head">SME Birchwood Circle</div>
      <p>Fragen?<br>Bitte nimm direkt<br>Kontakt mit uns auf.</p>
      <p>Lukas Brenner<br>sme@kvr-beispiel.ch</p>
    </div>
    <div class="sender" style="left:243px;top:292px;"><span class="sender__mark"></span><span class="sender__name">KVR</span></div>

    <div class="photo photo--table" role="img" aria-label="Runder weisser Tisch mit Laptops und Bürostühlen von oben" style="left:315px;top:0;width:349px;height:346px;"></div>
    <div class="badge" style="left:539px;top:18px;width:110px;height:110px;">
      <div class="badge__ring"></div><div class="badge__name" style="font-size:26px;">SME<br>BC</div>
    </div>
    <div class="title-tag" style="left:492px;top:277px;width:172px;height:43px;font-size:13.5px;">SME Birchwood Circle</div>
  </section>

  <!-- Title card -->
  <section class="panel" style="left:111px;top:418px;width:225px;height:344px;">
    <div class="photo photo--table" role="img" aria-label="Runder weisser Tisch mit Laptops und Bürostühlen von oben" style="inset:0;background:radial-gradient(circle at 0% 50%, #f2f2f2 0 45%, var(--grey-photo-a) 46% 70%, var(--grey-photo-b) 100%);"></div>
    <div class="badge" style="left:99px;top:15px;width:110px;height:110px;">
      <div class="badge__ring"></div><div class="badge__name" style="font-size:26px;">SME<br>BC</div>
    </div>
    <div class="title-tag" style="left:53px;top:274px;width:172px;height:43px;font-size:13.5px;">SME Birchwood Circle</div>
  </section>

  <!-- Back card -->
  <section class="panel" style="left:384px;top:418px;width:225px;height:344px;background:var(--white);">
    <div class="contact" style="right:129px;top:111px;">
      <div class="contact__head">SME Birchwood Circle</div>
      <p>Fragen?<br>Bitte nimm direkt<br>Kontakt mit uns auf.</p>
      <p>Lukas Brenner<br>sme@kvr-beispiel.ch</p>
    </div>
    <div class="sender" style="left:27px;top:292px;"><span class="sender__mark"></span><span class="sender__name">KVR</span></div>
    <div class="photo photo--table" role="img" aria-label="Runder weisser Tisch mit Laptops und Bürostühlen von oben" style="left:99px;top:0;width:126px;height:344px;background:radial-gradient(circle at 100% 50%, #f2f2f2 0 40%, var(--grey-photo-a) 41% 70%, var(--grey-photo-b) 100%);"></div>
  </section>

  <!-- Inside spread -->
  <section class="panel inner" style="left:111px;top:806px;width:664px;height:346px;background:var(--green);">
    <svg width="664" height="346" style="position:absolute;left:0;top:0;" aria-hidden="true">
      <polygon points="211,0 664,0 664,40 390,150 255,250" fill="var(--green-dark)"/>
      <polygon points="664,40 664,346 400,225 390,150" fill="var(--green-light)"/>
      <polygon points="255,250 400,225 664,346 250,346" fill="var(--green-mid)"/>
    </svg>

    <div class="block" style="left:16px;top:20px;">
      <h2>SME Call</h2>
      <p>Wir machen’s einfach. Und führen euch zwei-<br>wöchentlich durch eine 30 minütige Online-<br>Sitzung. Zur Abstimmung unserer Aktivitäten.</p>
      <h3>Halte dich kurz</h3>
      <p>Jeder Teilnehmer bekommt 3 min. Zeit, um<br>seine Angebote zu offenen Positionen und<br>Kandidaten möglichst kurz vorzutragen.<br>Je kürzer der ‚SME Call‘, umso besser.</p>
      <h3>Abstimmung ausserhalb</h3>
      <p>Ist jemand an einem Angebot interessiert,<br>dann soll er sein Interesse signalisieren.<br>Absprachen sind ausserhalb zu treffen,<br>nach dem ‚SME Call‘.</p>
      <h3>Jeder muss mitmachen</h3>
      <p>Interessierte können jederzeit teilnehmen.<br>Jeder Teilnehmer muss einen aktiven Beitrag<br>leisten und wird während dem ‚SME Call‘<br>kurz aufgerufen.</p>
      <h3>Kostenlos</h3>
      <p>Die Teilnahme am ‚SME BC‘ ist kostenlos.</p>
    </div>

    <div class="block" style="left:289px;top:16px;">
      <h2>SME Afterwork Event</h2>
      <p>Damit es persönlich ist und bleibt. Regelmässig treffen wir uns zu<br>einem Austausch. Viermal im Jahr in Zürich. Jeder kann und soll<br>seine Qualitäten persönlich präsentieren dürfen.</p>
    </div>

    <div class="block" style="left:465px;top:118px;">
      <h2>SME Platform</h2>
      <p>Lorem ipsum dolor sit amet, consectetuer<br>dipiscing elit.  Aenean commodo ligula eget<br>dolor. Aenean massa. Cum sociis natoque<br>penatibus et magnis dis parturient montes,<br>nascetur ridiculus mus. Donec quam felis,<br>ultricies nec, pellentesque eu, pretium quis,<br>sem.</p>
      <p>Nulla consequat massa quis enim. Donec<br>pede justo, fringilla vel, aliquet nec, vulputate</p>
    </div>

    <div class="block" style="left:355px;top:283px;">
      <h2>Los!</h2>
      <p>Nehmt regelmässig und aktiv teil, und ladet<br>Kollegen mit gesundem Potential dazu ein!</p>
    </div>

    <div class="badge" style="left:186px;top:81px;width:210px;height:210px;">
      <div class="badge__ring" style="border-width:9px;"></div><div class="badge__name" style="font-size:54px;">SME<br>BC</div>
    </div>
  </section>

</body>
</html>
```